Business Consulting Company requires a website design (PSD+HTML+CSS required)

Tarnvale Advisory is a Business Consulting Company that provides Analysis, Business Coaching and Systems and Document Design for clients.

We would like a simplistic yet professional looking website design that uses high quality imagery to project a professional persona across our entire site.

The completed project will need to include PSD files (for editing in Photoshop) and will need to also include HTML+CSS coded files that can be edited in Adobe Dreamweaver CS5.5.

Tarnvale Advisory currently has a functioning website (located at www.tarnvaleadvisory.com.au) but would like to replace its current site with something more professional, user friendly and content simplistic, with the overall design of this project being clean and very easy to navigate whilst remaining professionally focused.

A brief has been attached to this project to provide the key details but please feel free to contact me if you require any clarification or have any questions regarding the project.

Target Market(s)

The target audience for this website will be small to medium sized businesses (of all descriptions).

Industry/Entity Type

Business

Coding

Coded - Design and coding required

Number of Pages Required

5+ page

Requirements
Must have
• Simplistic design structure
• Professional images
• Easy to navigate
• Must be uploaded in PSD format
• Must be coded (HTML+CSS) and compatible with Adobe Dreamweaver CS5.5
Nice to have
• Use of the Company’s corporate colours throughout the site design
• Adding a Home page slider bar with images and short catchy messages (i.e. text based statements)
• Having a quick link box on each page that provides easy navigation throughout the site
• The use of different icons and images to depict our different services (i.e. a different icon and image for analysis service and coaching service etc.).
• All pages should follow a similar theme (universal approach to all pages)
Should not have
• When coding, images should not be used in place of text (all text must be editable)

```html
<!DOCTYPE html>
<html lang="en">
<head>
<meta charset="utf-8">
<title>Tarnvale Advisory</title>
<link rel="stylesheet" href="https://fonts.googleapis.com/css2?family=Open+Sans:wght@400;600;700;800&family=Arimo:wght@400&display=swap">
<style>
  :root {
    --blue: #009ad9;
    --grey: #5f6062;
    --light: #ececec;
    --white: #ffffff;
    --text: #333333;
    --arc: #5f6062;
  }
  * { margin: 0; padding: 0; box-sizing: border-box; }
  html, body { width: 1200px; height: 1196px; overflow: hidden; }
  body { position: relative; background: var(--white); font-family: "Open Sans", sans-serif; }

  .site-header { position: absolute; left: 0; top: 0; width: 1200px; height: 81px; background: var(--light); }
  .brand { position: absolute; top: 20px; display: flex; align-items: center; gap: 12px; }
  .brand-dot { width: 18px; height: 18px; border-radius: 50%; background: var(--blue); }
  .brand-name { font-weight: 700; font-size: 28px; color: var(--grey); letter-spacing: 0.5px; }
  .site-header .brand { left: 163px; }
  .phone { position: absolute; left: 863px; top: 30px; display: flex; align-items: center; gap: 12px;
           color: var(--blue); font-weight: 700; font-size: 16px; letter-spacing: 0.6px; }

  .main-nav { position: absolute; left: 0; top: 81px; width: 1200px; height: 36px; background: var(--grey);
              border-bottom: 3px solid var(--blue); }
  .nav-link { position: absolute; top: 0; height: 33px; line-height: 33px; color: var(--white);
              font-size: 12px; font-weight: 700; text-decoration: none; }
  .nav-link.is-active { background: var(--blue); text-align: center; }

  .hero { position: absolute; left: 0; top: 117px; width: 1200px; height: 345px;
          background: radial-gradient(ellipse at 40% 60%, #6b6762 0%, #3d3a37 45%, #1d1c1b 100%); }
  .hero-kicker { position: absolute; left: 413px; top: 132px; color: #f2f2f2; font-weight: 700;
                 font-size: 28px; letter-spacing: 1px; }
  .hero-title { position: absolute; left: 413px; top: 171px; color: #f2f2f2; font-weight: 800;
                font-size: 46px; letter-spacing: 1px; line-height: 1.2; }
  .hero-button { position: absolute; left: 496px; top: 248px; width: 249px; height: 47px;
                 border: 2px solid var(--blue); color: #f2f2f2; font-weight: 700; font-size: 17px;
                 text-align: center; line-height: 43px; letter-spacing: 0.5px; text-decoration: none; }

  .services { position: absolute; left: 0; top: 462px; width: 1200px; height: 207px; background: var(--blue); }
  .service { position: absolute; top: 22px; width: 260px; text-align: center; }
  .service svg { display: block; margin: 0 auto; }
  .service-title { margin-top: 12px; color: var(--white); font-weight: 700; font-size: 15px; letter-spacing: 0.3px; }

  .welcome { position: absolute; left: 163px; top: 738px; width: 860px; }
  .welcome h1 { color: var(--blue); font-weight: 700; font-size: 23px; letter-spacing: 0.3px; margin-bottom: 22px; }
  .welcome p { font-family: "Arimo", sans-serif; color: var(--text); font-size: 14px; line-height: 23px; margin-bottom: 26px; }

  .footer-nav { position: absolute; left: 0; top: 1002px; width: 1200px; height: 74px; background: var(--grey); }
  .footer-nav .nav-link { top: 21px; }

  .site-footer { position: absolute; left: 0; top: 1076px; width: 1200px; height: 120px; background: var(--light); }
  .site-footer .brand { left: 0; width: 1200px; justify-content: center; top: 32px; }
  .copyright { position: absolute; left: 0; top: 90px; width: 1200px; text-align: center;
               color: var(--blue); font-weight: 700; font-size: 11px; letter-spacing: 0.3px; }
</style>
</head>
<body>
  <header class="site-header">
    <div class="brand"><span class="brand-dot"></span><span class="brand-name">Tarnvale Advisory</span></div>
    <div class="phone">(03) 52 90 4417
      <svg width="14" height="22" viewBox="0 0 14 22" aria-hidden="true">
        <rect x="1" y="1" width="12" height="20" rx="2" fill="none" stroke="#5f6062" stroke-width="2"/>
        <rect x="3" y="4" width="8" height="11" fill="#5f6062"/>
        <circle cx="7" cy="18" r="1.2" fill="#5f6062"/>
      </svg>
    </div>
  </header>

  <nav class="main-nav">
    <a class="nav-link is-active" href="#" style="left:604px;width:85px">Home</a>
    <a class="nav-link" href="#" style="left:708px">About Us</a>
    <a class="nav-link" href="#" style="left:788px">Services</a>
    <a class="nav-link" href="#" style="left:874px">Contact Us</a>
    <a class="nav-link" href="#" style="left:957px">Testimonial</a>
  </nav>

  <section class="hero" role="img" aria-label="Photograph of a laptop on a wooden desk with a glass of water, softly blurred">
    <p class="hero-kicker">WE TAKE THE PAIN OUT OF</p>
    <p class="hero-title">DOING BUSINESS</p>
    <a class="hero-button" href="#">READ MORE</a>
  </section>

  <section class="services">
    <div class="service" style="left:114px">
      <svg width="130" height="130" viewBox="0 0 130 130" aria-hidden="true">
        <path d="M1 65 A64 64 0 0 1 129 65" fill="none" stroke="#5f6062" stroke-width="5"/>
        <circle cx="65" cy="65" r="59" fill="#fff"/>
        <rect x="36" y="62" width="11" height="26" fill="#5f6062"/>
        <rect x="51" y="68" width="11" height="20" fill="#5f6062"/>
        <rect x="66" y="58" width="11" height="30" fill="#5f6062"/>
        <rect x="81" y="48" width="11" height="40" fill="#5f6062"/>
        <rect x="34" y="91" width="60" height="4" fill="#5f6062"/>
        <polyline points="36,60 50,48 63,56 86,36" fill="none" stroke="#009ad9" stroke-width="5"/>
        <polygon points="80,30 94,28 92,42" fill="#009ad9"/>
      </svg>
      <p class="service-title">BUSINESS ANALYSIS</p>
    </div>
    <div class="service" style="left:452px">
      <svg width="130" height="130" viewBox="0 0 130 130" aria-hidden="true">
        <path d="M1 65 A64 64 0 0 1 129 65" fill="none" stroke="#5f6062" stroke-width="5"/>
        <circle cx="65" cy="65" r="59" fill="#fff"/>
        <rect x="40" y="42" width="54" height="42" fill="none" stroke="#009ad9" stroke-width="4"/>
        <line x1="36" y1="42" x2="98" y2="42" stroke="#5f6062" stroke-width="4"/>
        <line x1="36" y1="86" x2="98" y2="86" stroke="#5f6062" stroke-width="4"/>
        <line x1="26" y1="90" x2="48" y2="70" stroke="#5f6062" stroke-width="4"/>
      </svg>
      <p class="service-title">BUSINESS COACHING</p>
    </div>
    <div class="service" style="left:806px">
      <svg width="130" height="130" viewBox="0 0 130 130" aria-hidden="true">
        <path d="M1 65 A64 64 0 0 1 129 65" fill="none" stroke="#5f6062" stroke-width="5"/>
        <circle cx="65" cy="65" r="59" fill="#fff"/>
        <polyline points="28,86 50,70 66,80 94,54" fill="none" stroke="#5f6062" stroke-width="7"/>
        <polygon points="86,46 106,42 102,62" fill="#5f6062"/>
        <polyline points="28,72 50,56 66,66 84,50" fill="none" stroke="#009ad9" stroke-width="5"/>
      </svg>
      <p class="service-title">BUSINESS DEVELOPMENT</p>
    </div>
  </section>

  <main class="welcome">
    <h1>Welcome to Tarnvale Advisory</h1>
    <p>Tarnvale Advisory is a business analysis, coaching and business development provider who specialises in assisting businesses to achieve maximum efficiency, increased productivity and who can assist with improving a business’s overall profitability.</p>
    <p>At Tarnvale, we pride ourselves on our ability to form strong client relationships whilst delivering impressive results. For us, it’s all about effective communication coupled with practical and measurable results!</p>
  </main>

  <nav class="footer-nav">
    <a class="nav-link" href="#" style="left:401px">Home</a>
    <a class="nav-link" href="#" style="left:479px">About Us</a>
    <a class="nav-link" href="#" style="left:559px">Services</a>
    <a class="nav-link" href="#" style="left:646px">Contact Us</a>
    <a class="nav-link" href="#" style="left:728px">Testimonial</a>
  </nav>

  <footer class="site-footer">
    <div class="brand"><span class="brand-dot"></span><span class="brand-name">Tarnvale Advisory</span></div>
    <p class="copyright">Copyright © 2014 Privacy Policy</p>
  </footer>
</body>
</html>
```